Create a pouch design for a new sports supplement product

Dimensions are 235mm (width) x 335mm (length) x 110mm (gusset)
File 1 - Extension of design brief please read both briefs
File 2 - Is 2 potential pouches this is just to give you a better example of size the dimensions are for the pouch on the right. This picture is not to give you design ideas as I am not very keen on either of these designs.
We need a design to be printed onto the pouches of our whey protein product. The brand name is 'Stellar Fuelworks' and needs to be displayed on the packaging either just writing or a simple logo design. I am not the most creative person in the world but have put together a more detailed brief listing some of the key information that needs to be included on the pouch (See attachment) Please feel free if you have experience of this the sports supplement market or have different ideas then please feel free to explore them.
The pouch would either be printed straight onto the pouch, or possibly just a printed label (front & back) to be stuck onto the pouch. Please design either or both.
Open to different colour schemes. Design has to be modern looking and eye-catching.
Some key points;
High quality whey protein concentrate
All Natural
Soy free
Great tasting
Please google image search 'protein pouches' to see other designs if your not familiar with the sports supplement market.
Any questions feel free to ask.
Updates
Hi, Thanks for all your design! I am really busy at the moment so haven't had chance to give feedback and have a proper look through all the designs. I have extended the time frame to give myself chance to give proper feedback and see any changes needed. Expect feedback sunday at the latest, and I will be pick a design early next week.
Target Market(s)
Sports supplement market. Product is a whey protein shake
Industry/Entity Type
Nutrition
Look and feel
Each slider illustrates characteristics of the customer's brand and the style your logo design should communicate.

```html
<!DOCTYPE html>
<html lang="en">
<head>
<meta charset="utf-8">
<title>Stellar Fuelworks – Natural Whey Protein Pouch</title>
<link rel="stylesheet" href="https://fonts.googleapis.com/css2?family=Anton&family=Roboto+Condensed:wght@400;700&display=swap">
<style>
  :root {
    --page-bg: #ffffff;
    --brand-orange: #f27a1c;
    --label-white: #ffffff;
    --ink-black: #151515;
    --rule-grey: #9a9a9a;
    --claim-red: #d0112b;
    --flavour-bar: #1c1c1c;
    --silver-light: #f2f2f2;
    --silver-dark: #9c9c9c;
    --green-core: #3f8a2c;
    --green-mid: #1d4a17;
    --green-edge: #060b05;
    --red-core: #c3123d;
    --red-mid: #5c0a1f;
    --red-edge: #0c0205;
  }
  * { box-sizing: border-box; margin: 0; padding: 0; }
  html, body {
    width: 1200px;
    height: 982px;
    overflow: hidden;
    background: var(--page-bg);
  }
  .pouch-range {
    position: relative;
    width: 1200px;
    height: 982px;
  }
  .pouch {
    position: absolute;
    top: 96px;
    width: 420px;
    height: 790px;
    border-radius: 14px;
    overflow: hidden;
    font-family: "Anton", "Roboto Condensed", sans-serif;
  }
  .pouch--green {
    left: 140px;
    --core: var(--green-core);
    --mid: var(--green-mid);
    --edge: var(--green-edge);
  }
  .pouch--red {
    left: 670px;
    --core: var(--red-core);
    --mid: var(--red-mid);
    --edge: var(--red-edge);
  }
  .pouch__background {
    position: absolute;
    inset: 0;
    background:
      radial-gradient(ellipse 55% 28% at 50% 12%, rgba(255,255,255,0.55), rgba(255,255,255,0) 70%),
      radial-gradient(ellipse 90% 60% at 50% 55%, var(--core) 0%, var(--mid) 45%, var(--edge) 100%);
  }
  .pouch__top-seal {
    position: absolute;
    top: 0; left: 0; right: 0;
    height: 34px;
    background: linear-gradient(180deg, rgba(0,0,0,0.55), rgba(0,0,0,0));
  }
  .brand-name {
    position: absolute;
    top: 72px;
    left: 0; right: 0;
    text-align: center;
    color: var(--brand-orange);
    font-size: 46px;
    line-height: 0.98;
    letter-spacing: 0.5px;
  }
  .product-label {
    position: absolute;
    top: 268px;
    left: 18px;
    width: 384px;
    height: 310px;
    background: var(--label-white);
    clip-path: polygon(14% 0, 86% 0, 100% 50%, 86% 100%, 14% 100%, 0 50%);
    text-align: center;
  }
  .product-label__rule {
    position: absolute;
    left: 62px; right: 62px;
    height: 3px;
    background: var(--rule-grey);
  }
  .product-label__rule--top { top: 14px; }
  .product-label__name {
    position: absolute;
    top: 34px;
    left: 0; right: 0;
    color: var(--ink-black);
    line-height: 1;
  }
  .product-label__line { display: block; font-size: 58px; line-height: 1.02; }
  .product-label__line--large { font-size: 82px; line-height: 1.02; }
  .product-label__claims {
    position: absolute;
    top: 242px;
    left: 56px; right: 56px;
    display: flex;
    justify-content: center;
    font-family: "Roboto Condensed", sans-serif;
    font-size: 11px;
    line-height: 1.15;
    color: var(--claim-red);
    text-align: left;
  }
  .claim {
    padding: 0 6px;
    border-left: 1px solid var(--claim-red);
  }
  .claim:first-child { border-left: none; padding-left: 0; }
  .flavour-bar {
    position: absolute;
    top: 620px;
    left: 68px;
    width: 232px;
    height: 54px;
    background: var(--flavour-bar);
    color: var(--label-white);
    font-family: "Roboto Condensed", sans-serif;
    font-weight: 700;
    font-size: 16px;
    line-height: 1.1;
    text-align: center;
    display: flex;
    align-items: center;
    justify-content: center;
  }
  .serving-info {
    position: absolute;
    top: 594px;
    right: 8px;
    width: 110px;
    text-align: right;
    color: var(--label-white);
  }
  .serving-info__count { display: block; font-size: 62px; line-height: 1; }
  .serving-info__unit {
    display: block;
    font-family: "Roboto Condensed", sans-serif;
    font-weight: 700;
    font-style: italic;
    font-size: 22px;
    line-height: 1;
    margin-top: -4px;
  }
  .serving-info__weight {
    display: block;
    font-family: "Roboto Condensed", sans-serif;
    font-size: 22px;
    margin-top: 6px;
  }
  .pouch__bottom-band {
    position: absolute;
    left: 0; right: 0; bottom: 0;
    height: 78px;
    background: linear-gradient(180deg, var(--silver-dark) 0%, var(--silver-light) 35%, #d4d4d4 65%, var(--silver-dark) 100%);
  }
</style>
</head>
<body>
<main class="pouch-range">

  <section class="pouch pouch--green" aria-label="Stellar Fuelworks Natural Whey Protein, green pouch">
    <div class="pouch__background" role="img" aria-label="Dark green burst with halftone dot texture"></div>
    <div class="pouch__top-seal"></div>
    <h1 class="brand-name">STELLAR<br>FUELWORKS</h1>
    <div class="product-label">
      <div class="product-label__rule product-label__rule--top"></div>
      <h2 class="product-label__name">
        <span class="product-label__line">NATURAL</span>
        <span class="product-label__line">WHEY</span>
        <span class="product-label__line product-label__line--large">PROTEIN</span>
      </h2>
      <ul class="product-label__claims">
        <li class="claim" style="list-style:none">No artificial<br>Flavours</li>
        <li class="claim" style="list-style:none">Excellent<br>Amino acid profile</li>
        <li class="claim" style="list-style:none">80% high quality<br>protein content</li>
        <li class="claim" style="list-style:none">Soy free</li>
      </ul>
    </div>
    <div class="flavour-bar">STRAWBERRY<br>FLAVOUR</div>
    <div class="serving-info">
      <span class="serving-info__count">30</span>
      <span class="serving-info__unit">servings</span>
      <span class="serving-info__weight">909g</span>
    </div>
    <div class="pouch__bottom-band"></div>
  </section>

  <section class="pouch pouch--red" aria-label="Stellar Fuelworks Natural Whey Protein, red pouch">
    <div class="pouch__background" role="img" aria-label="Dark red burst with halftone dot texture"></div>
    <div class="pouch__top-seal"></div>
    <h1 class="brand-name">STELLAR<br>FUELWORKS</h1>
    <div class="product-label">
      <div class="product-label__rule product-label__rule--top"></div>
      <h2 class="product-label__name">
        <span class="product-label__line">NATURAL</span>
        <span class="product-label__line">WHEY</span>
        <span class="product-label__line product-label__line--large">PROTEIN</span>
      </h2>
      <ul class="product-label__claims">
        <li class="claim" style="list-style:none">No artificial<br>Flavours</li>
        <li class="claim" style="list-style:none">Excellent<br>Amino acid profile</li>
        <li class="claim" style="list-style:none">80% high quality<br>protein content</li>
        <li class="claim" style="list-style:none">Soy free</li>
      </ul>
    </div>
    <div class="flavour-bar">STRAWBERRY<br>FLAVOUR</div>
    <div class="serving-info">
      <span class="serving-info__count">30</span>
      <span class="serving-info__unit">servings</span>
      <span class="serving-info__weight">909g</span>
    </div>
    <div class="pouch__bottom-band"></div>
  </section>

</main>
</body>
</html>
```